Powerpoint visual improvements

I need a cover page, and our beliefs page and differentiating factors page / graphic design for our presentation. For the cover page I would just like an attractive design that incorporate our architectural concept with columns and potentially our logo. For the beliefs page I just want a more attractive presentatoin of the concepts. For the differentiating factors page I want a graphic that captures the points about how we are different from competitors. I have used the attached content to date, but I think it can be improved. The text is included in the graphic and I would also like to make sure the firm logo is incorporated.

Target Market(s)

Individual and institutional investors.

Industry/Entity Type

Investment Advisory

Requirements
Must have
• Our corporate colors are generally RGB 145,148,149; 66,68,76; 0,0,153; and 0,63,127. Our logo is attached. Our primary font is Georgia. Our website is www.VorlineCP.com. The key pages are www.VorlineCP.com/beliefs and www.VorlineCP.com/value we are trying to capture in a presentation. We also need a new presentation cover. Use the website as a reference for the type of imagery we like.

```html
<!DOCTYPE html>
<html lang="en">
<head>
<meta charset="utf-8">
<title>Vorline Asset Management – Presentation Pages</title>
<link rel="stylesheet" href="https://fonts.googleapis.com/css2?family=Gelasio:wght@400;700&family=Open+Sans:wght@300;400&display=swap">
<style>
:root{
  --board:#a6a6a6;
  --navy:#1c1ca6;
  --navy-deep:#12127e;
  --gray:#919495;
  --slate:#42444c;
  --paper:#ffffff;
  --ink:#4a4c54;
  --stone-light:#d9d2c3;
  --stone-dark:#6d655a;
}
*{margin:0;padding:0;box-sizing:border-box}
html,body{width:743px;height:1200px;overflow:hidden}
body{background:var(--board);position:relative;font-family:"Open Sans",sans-serif;color:var(--ink)}
.page{position:absolute;width:329px;height:248px;overflow:hidden;background:var(--paper);box-shadow:0 1px 3px rgba(0,0,0,.35)}
.page-label{position:absolute;width:329px;text-align:center;font-family:"Open Sans",sans-serif;font-size:14px;color:#111;letter-spacing:.3px}
.photo{position:absolute;inset:0}
.grid-line{position:absolute;background:var(--paper)}
.url{position:absolute;bottom:5px;left:127px;font-size:5px;letter-spacing:1.2px;color:var(--slate)}
.url.light{color:var(--paper)}
.rule{position:absolute;bottom:8px;height:.6px;background:var(--gray)}
.rule.light{background:var(--paper)}
.folio{position:absolute;right:8px;bottom:5px;font-size:5px;color:var(--slate)}
.folio.light{color:var(--paper)}
.mini-brand{position:absolute;left:8px;top:8px;display:flex;align-items:center;gap:3px}
.mini-brand .dot{width:15px;height:15px;border-radius:50%;background:var(--gray)}
.mini-brand .name{font-family:"Open Sans",sans-serif;font-weight:300;font-size:10px;color:var(--gray)}
.pill{position:absolute;background:var(--navy);color:var(--paper);font-family:Gelasio,Georgia,serif;font-weight:700;font-size:8.5px;letter-spacing:.3px;padding:1px 10px;border-radius:8px;white-space:nowrap;line-height:11px}
.body-copy{font-family:Gelasio,Georgia,serif;color:var(--ink)}
/* cover */
.cover-band{position:absolute;left:0;top:82px;width:218px;height:80px;background:var(--navy);display:flex;align-items:center;padding-left:29px;gap:8px}
.brand-circle{border-radius:50%;background:var(--paper)}
.brand-name{font-family:"Open Sans",sans-serif;font-weight:300;color:var(--paper);line-height:1}
.brand-sub{font-family:"Open Sans",sans-serif;font-weight:300;color:var(--paper);letter-spacing:.3px}
/* who we are */
.who-title{position:absolute;left:177px;top:94px;width:100px;text-align:center;color:var(--paper);font-family:Gelasio,Georgia,serif;line-height:1}
.who-title .big{font-size:26px;font-weight:700;display:block}
.who-title .small{font-size:17px;display:block;margin-top:3px}
/* story */
.story-copy{position:absolute;left:7px;top:84px;width:136px;font-size:5.6px;line-height:1.6}
.story-copy p{margin-bottom:6px}
/* difference */
.diff-panel{position:absolute;left:106px;top:31px;width:116px;height:185px}
.diff-label{position:absolute;font-family:Gelasio,Georgia,serif;font-weight:700;font-size:4.6px;color:var(--paper);letter-spacing:.2px}
.diff-note{position:absolute;width:76px;font-size:3.6px;line-height:1.4;text-align:center}
.diff-note.right{text-align:justify}
/* beliefs */
.belief{position:absolute;font-size:4.3px;line-height:1.5}
.belief h3{font-family:Gelasio,Georgia,serif;font-weight:700;font-size:5.6px;color:var(--navy);margin-bottom:1px;letter-spacing:.2px}
/* process */
.process-panel{position:absolute;left:205px;top:0;width:124px;height:248px;background:var(--navy);padding:12px 8px 0 8px;color:var(--paper);font-size:3.9px;line-height:1.55;text-align:justify}
.process-panel p{margin-bottom:5px}
/* back */
.contact-box{position:absolute;left:110px;top:84px;width:108px;height:80px;background:var(--navy);color:var(--paper);text-align:center;padding-top:9px}
.contact-box h2{font-family:Gelasio,Georgia,serif;font-size:9.5px;font-weight:700;letter-spacing:.3px;margin-bottom:7px}
.contact-line{font-size:3.7px;line-height:8.3px;display:flex;justify-content:center;align-items:center;gap:3px}
.contact-line i{display:inline-block;width:3.5px;height:3.5px;border-radius:50%;background:var(--paper)}
.badge{position:absolute;left:142px;width:46px;border-radius:2px}
/* showcase */
.show-brand{position:absolute;left:440px;top:915px;width:218px;text-align:center;color:var(--paper)}
</style>
</head>
<body>

<!-- Cover -->
<section class="page" style="left:29px;top:22px">
  <div class="photo" role="img" aria-label="Photograph of a sunlit stone colonnade casting column shadows on paving" style="background:linear-gradient(180deg,#e9e2d3 0%,#c9bda8 30%,#8e8372 55%,#b6ab98 75%,#6f6658 100%)"></div>
  <div class="grid-line" style="left:0;top:82px;width:329px;height:1px"></div>
  <div class="grid-line" style="left:218px;top:82px;width:1px;height:166px"></div>
  <div class="grid-line" style="left:0;top:162px;width:329px;height:1.5px"></div>
  <div class="grid-line" style="left:109px;top:162px;width:1.5px;height:86px"></div>
  <div class="grid-line" style="left:218px;top:0;width:1px;height:82px"></div>
  <div class="cover-band">
    <div class="brand-circle" style="width:62px;height:62px"></div>
    <div>
      <div class="brand-name" style="font-size:28px">Vorline</div>
      <div class="brand-sub" style="font-size:8px;margin-top:3px">ASSET MANAGEMENT</div>
    </div>
  </div>
</section>
<div class="page-label" style="left:29px;top:274px">COVER PAGE</div>

<!-- Page 01 -->
<section class="page" style="left:386px;top:22px">
  <div class="photo" role="img" aria-label="Photograph of a row of fluted stone columns on a polished floor" style="background:linear-gradient(90deg,#5e574b 0%,#d8cfbd 12%,#8a8171 22%,#e3dccb 34%,#8c8373 46%,#d5ccb9 58%,#7f7767 70%,#c9bfac 82%,#6a6357 100%)"></div>
  <svg width="329" height="248" style="position:absolute;inset:0">
    <polygon points="227,58 293,124 227,190 161,124" fill="var(--navy)"/>
    <polygon points="227,66 285,124 227,182 169,124" fill="none" stroke="var(--paper)" stroke-width=".8"/>
  </svg>
  <div class="who-title"><span class="big">WHO</span><span class="small">WE ARE</span></div>
  <div class="rule light" style="left:40px;width:84px"></div>
  <div class="url light">www.VorlineCP.com</div>
  <div class="folio light">01</div>
</section>
<div class="page-label" style="left:386px;top:274px">PAGE 01</div>

<!-- Page 02 -->
<section class="page" style="left:29px;top:314px">
  <div class="mini-brand"><span class="dot"></span><span class="name">Vorline</span></div>
  <div class="pill" style="left:0;top:62px;border-radius:0 8px 8px 0;padding-left:8px">OUR STORY</div>
  <div class="story-copy body-copy">
    <p>Vorline (vor-line) is an architectural term used to describe a slight curve given to the shaft of a column to correct for the illusion of concavity.</p>
    <p>We chose the name Vorline because we believe most investors pay premium fees for overly complex portfolios, creating the illusion of value.</p>
    <p>It is the mission of our firm to use our combined decades of investment experience to develop low cost, understandable portfolios to correct for that illusion and increase potential return outcomes for clients.</p>
  </div>
  <svg width="329" height="248" style="position:absolute;inset:0" role="img" aria-label="Photograph of a curved modern glass and stone office building">
    <defs><linearGradient id="bldg" x1="0" y1="0" x2="1" y2="1"><stop offset="0" stop-color="#2f4f86"/><stop offset=".45" stop-color="#c9bba6"/><stop offset=".7" stop-color="#7c7264"/><stop offset="1" stop-color="#3c5d95"/></linearGradient></defs>
    <polygon points="275,0 329,0 329,248 245,248 150,125" fill="url(#bldg)"/>
    <polygon points="181,180 205,204 181,228 157,204" fill="#c8c8c8"/>
  </svg>
  <div class="rule" style="left:122px;width:4px"></div>
  <div class="url">www.VorlineCP.com</div>
  <div class="rule" style="left:200px;width:110px"></div>
  <div class="folio">02</div>
</section>
<div class="page-label" style="left:29px;top:569px">PAGE 02</div>

<!-- Page 03 -->
<section class="page" style="left:386px;top:314px">
  <div class="mini-brand"><span class="dot"></span><span class="name">Vorline</span></div>
  <div class="pill" style="left:88px;top:7px">THE VORLINE DIFFERENCE</div>
  <div class="diff-panel" role="img" aria-label="Photograph of a blue-tinted glass office facade" style="background:linear-gradient(160deg,#2a54a8 0%,#1b3f8f 50%,#123380 100%)"></div>
  <svg width="329" height="248" style="position:absolute;inset:0">
    <line x1="163" y1="36" x2="163" y2="212" stroke="var(--paper)" stroke-width=".8"/>
    <g fill="var(--paper)" stroke="var(--navy)" stroke-width=".6">
      <circle cx="163" cy="47" r="4"/><circle cx="163" cy="78" r="4"/><circle cx="163" cy="109" r="4"/>
      <circle cx="163" cy="139" r="4"/><circle cx="163" cy="170" r="4"/><circle cx="163" cy="201" r="4"/>
    </g>
  </svg>
  <div class="diff-label" style="left:171px;top:44px">EXPERIENCE</div>
  <div class="diff-label" style="left:110px;top:75px;width:45px;text-align:right">INDEPENDENCE</div>
  <div class="diff-label" style="left:171px;top:106px">ACCOUNTABILITY</div>
  <div class="diff-label" style="left:110px;top:136px;width:45px;text-align:right">ALIGNMENT</div>
  <div class="diff-label" style="left:171px;top:167px">FOCUS</div>
  <div class="diff-label" style="left:110px;top:198px;width:45px;text-align:right">TRANSPARENCY</div>
  <p class="diff-note body-copy" style="left:20px;top:68px">We are majority-owned by our team. The firm has no ties to other firms, and every recommendation is built solely for clients.</p>
  <p class="diff-note body-copy" style="left:20px;top:124px">We do the research and build each portfolio ourselves. Our process is distinct, disciplined and designed to find sound long-term investments.</p>
  <p class="diff-note body-copy" style="left:20px;top:188px">We believe in clear, regular communication. If we cannot explain it simply, we do not own it, and clients always know why.</p>
  <p class="diff-note right body-copy" style="left:232px;top:40px">Our founders bring decades of combined experience in investment analysis, portfolio construction, due diligence and security selection.</p>
  <p class="diff-note right body-copy" style="left:232px;top:96px">We own our recommendations and follow a methodical, patient approach to selecting investments, with close review of every manager and decision.</p>
  <p class="diff-note right body-copy" style="left:232px;top:155px">We focus on our strengths and invest where we hold a real research edge, avoiding complex products that miss our standards.</p>
  <div class="rule" style="left:122px;width:4px"></div>
  <div class="url">www.VorlineCP.com</div>
  <div class="rule" style="left:200px;width:110px"></div>
  <div class="folio">03</div>
</section>
<div class="page-label" style="left:386px;top:569px">PAGE 03</div>

<!-- Page 04 -->
<section class="page" style="left:29px;top:606px">
  <div class="mini-brand"><span class="dot"></span><span class="name">Vorline</span></div>
  <div class="pill" style="left:114px;top:6px">OUR BELIEFS</div>
  <div class="belief body-copy" style="left:85px;top:38px;width:160px;text-align:center">
    <h3>COST MATTERS</h3>
    We believe the average investor pays too much for investment planning and portfolio advice. We also believe that costs quickly limit the potential for wealth compounding. Our fee schedule is designed to be below industry averages.
  </div>
  <div class="belief body-copy" style="left:15px;top:102px;width:95px">
    <h3>ACCESS MATTERS</h3>
    We believe everyone should have access to an experienced investment professional and high quality asset management. Our account minimums, fees and portfolios reflect this conviction.
  </div>
  <div class="belief body-copy" style="left:219px;top:102px;width:96px;text-align:right">
    <h3>RESEARCH MATTERS</h3>
    We believe that accountability and thorough, grass roots research is critical to generating outsized returns. Our founders average more than 15 years of investment experience and we conduct all of our research in house.
  </div>
  <div role="img" aria-label="Illustration of four interlocking puzzle pieces with cost, access, research and focus icons" style="position:absolute;left:117px;top:86px;width:92px;height:80px;border-radius:6px;background:radial-gradient(circle,#6d6f77 0%,#2a2aa8 60%,rgba(255,255,255,0) 72%)"></div>
  <div class="belief body-copy" style="left:85px;top:172px;width:160px;text-align:center">
    <h3>FOCUS MATTERS</h3>
    We believe investment planning and investment options have gotten overly complex and excessively engineered. We also believe that this complexity creates unnecessary distractions that limit return outcomes. Our portfolios are focused on a well-diversified group of investments that our clients can understand.
  </div>
  <div class="rule" style="left:122px;width:4px"></div>
  <div class="url">www.VorlineCP.com</div>
  <div class="rule" style="left:200px;width:110px"></div>
  <div class="folio">04</div>
</section>
<div class="page-label" style="left:29px;top:860px">PAGE 04</div>

<!-- Page 05 -->
<section class="page" style="left:386px;top:606px">
  <div class="mini-brand"><span class="dot"></span><span class="name">Vorline</span></div>
  <div class="pill" style="left:0;top:40px;border-radius:0 8px 8px 0;padding-left:7px">OUR INVESTMENT PROCESS</div>
  <div role="img" aria-label="Photograph of a bright office interior with windows and a plant, framed in a circle" style="position:absolute;left:24px;top:60px;width:156px;height:156px;border-radius:50%;background:linear-gradient(120deg,#9a7a55 0%,#e8e6ea 35%,#c7c1cf 60%,#7a5d40 100%)"></div>
  <div class="process-panel">
    <p>At Vorline Asset Management, we believe that a methodical research process and a deep understanding of investments are necessary to build high-conviction portfolios, which are the foundation for risk-adjusted outperformance relative to the broad market over a complete market cycle.</p>
    <p>We utilize a combination of bottom-up investment manager and security analysis, along with top-down macro analysis to build optimal risk-adjusted portfolios. Our risk-conscious, diversified approach may invest in actively-managed equity, fixed income, alternative and mixed-asset investment products and liquid, individual securities.</p>
    <p>Portfolios are constructed through the implementation of our Core / Completion philosophy and incorporate each client's tax situation, investment goals, time horizon and risk tolerance, among other factors. Our Core / Completion philosophy was developed over time through extensive research into broad asset classes, sub-asset classes, interaction of those asset classes with one another, and the probability of active manager success over a complete market cycle. All of our asset allocation decisions rely on our investment manager research process, individual security research process and our decision making structure for investment vehicles.</p>
  </div>
  <div class="rule" style="left:122px;width:4px"></div>
  <div class="url">www.VorlineCP.com</div>
  <div class="folio light">05</div>
</section>
<div class="page-label" style="left:386px;top:860px">PAGE 05</div>

<!-- Back page -->
<section class="page" style="left:29px;top:898px">
  <div class="photo" role="img" aria-label="Photograph of slender columns reflected on a polished wooden floor" style="background:linear-gradient(180deg,#8d8e92 0%,#b7b3ab 30%,#6e5a44 55%,#8d7458 80%,#5b4735 100%)"></div>
  <div class="grid-line" style="left:109px;top:0;width:1.5px;height:248px"></div>
  <div class="grid-line" style="left:219px;top:0;width:1.5px;height:248px"></div>
  <div class="grid-line" style="left:0;top:82px;width:329px;height:1.5px"></div>
  <div class="grid-line" style="left:0;top:164px;width:329px;height:1.5px"></div>
  <div style="position:absolute;left:110px;top:18px;width:108px;text-align:center">
    <div class="brand-circle" style="width:30px;height:30px;margin:0 auto"></div>
    <div class="brand-name" style="font-size:13px;margin-top:4px">Vorline</div>
    <div class="brand-sub" style="font-size:4.5px;margin-top:1px">ASSET MANAGEMENT</div>
  </div>
  <div class="contact-box">
    <h2>CONTACT US</h2>
    <div class="contact-line"><i></i>418 Harlow Pkwy, Suite 310, Easton, WI 53100</div>
    <div class="contact-line"><i></i>Mon – Friday (8am – 5pm)</div>
    <div class="contact-line"><i></i>1-800-555-0142</div>
    <div class="contact-line"><i></i>info@vorlinecp.com</div>
    <div class="contact-line"><i></i>www.vorlinecp.com</div>
  </div>
  <div class="badge" style="top:178px;height:17px;background:#d8e6f2"></div>
  <div class="badge" style="top:199px;height:14px;background:#111"></div>
  <div class="badge" style="top:217px;height:14px;background:#111"></div>
</section>
<div class="page-label" style="left:29px;top:1154px">BACK PAGE</div>

<!-- Brand showcase -->
<div class="show-brand">
  <div class="brand-circle" style="width:128px;height:128px;margin:0 auto"></div>
  <div class="brand-name" style="font-size:50px;margin-top:18px">Vorline</div>
  <div class="brand-sub" style="font-size:15px;margin-top:8px">ASSET MANAGEMENT</div>
</div>

</body>
</html>
```